Velmor PashuのRTZの電子書籍表紙デザインをお願いします。

*週末ごとに和みを探す読者へ贈る癒やしの四季手帳*というタイトルの表紙デザインの発注です。
サブタイトル 猫の昼寝は街を照らす
猫の昼寝は毎日を照らす
私は猫の昼寝に癒された
になります。
お笑い要素の多い1日1笑いみたいな本の表紙です。

初めての表紙デザイン依頼なので、よく勝手がわかっていませんので、
出来上がったデザインを作家グループの中で投票にかけて、
一番投票得票数の多かったものを表紙デザインとして選ばせていただきたいと考えております。
もしかしたら、その中で、何か修正依頼など来るかもしれませんが、
それも含めて、ご対応していただける方よろしくお願いします。

1部内容の抜粋を記載します。

その他何かご不明な点がございましたら、お気軽にご質問下さい。
よろしくお願いいたします。
すいません。作家名は後でお伝えします。作家名もどこかに挿入いただきたいです。よろしくお願いします。
データサイズですが、推奨サイズでJPEGファイルでご納品下さい、よろしくお願いします。
皆様、たくさんのご応募まことにありがとうございました。
現在、作家グループへ全体回覧のメールを致しました。
皆様の投票結果までお待ちください。
また、この度、いろいろな作品に触れさせていただきましたこと本当に
本当に感謝いたします。
今回の表紙に関しましては、どうしても1名しか選べない状況がございますこと
また、選挙による投票にて決定致しますこと、ご理解何卒よろしくお願い申しあげます。
また、もしも、今回当選に至らないことがありましても、
今後も私自身は作家生活を継続予定ですので、
(今回は作品の表紙に合わないことがあっても)作風の気に入ったデザイナー様には
個人的にお話を相談させていただく場合もあると思っております。
その際には何卒よろしくお願い申し上げます。この度はまことにありがとうございました。
この度はご応募まことにありがとうございました。厳選なる選挙の結果、1名の作家さんが選ばれました。
選ばれました方には個別にお伝えいたしております。この度はまことにご応募ありがとうございました。

作家メンバーによる総選挙にて決定させて頂きました。皆様に広く愛される作品で、投票数も多く選ばせて頂きました。誠にありがとうございました。

今回、誠にご提案ありがとうございました。私自身は作家活動を継続していくつもりですので、また、個別にご依頼させて頂くこともあるかと思います。その時はよろしくお願いします。この度はありがとうございました。

```html
<!DOCTYPE html>
<html lang="ja">
<head>
<meta charset="utf-8">
<title>癒やしの四季手帳 表紙</title>
<link rel="stylesheet" href="https://fonts.googleapis.com/css2?family=M+PLUS+Rounded+1c:wght@700;800;900&display=swap">
<style>
  :root {
    --orange: #f39200;
    --orange-deep: #e07800;
    --white: #ffffff;
    --green: #5cb531;
    --pink: #e5177f;
    --blue: #1c9ee0;
    --red: #e6332a;
    --gray: #8a8a8a;
    --skin-light: #f2d3bd;
    --skin-mid: #d9a586;
    --skin-dark: #8a5a45;
  }
  * { margin: 0; padding: 0; box-sizing: border-box; }
  html, body { width: 751px; height: 1200px; overflow: hidden; background: var(--white); }
  .cover {
    position: relative;
    width: 751px; height: 1200px;
    overflow: hidden;
    font-family: "M PLUS Rounded 1c", sans-serif;
  }
  .cover-photo {
    position: absolute; inset: 0;
    background:
      radial-gradient(ellipse 62% 48% at 50% 78%, var(--skin-mid) 0%, var(--skin-light) 55%, rgba(242,211,189,0) 80%),
      radial-gradient(ellipse 40% 30% at 20% 55%, var(--skin-dark) 0%, rgba(138,90,69,0) 70%),
      linear-gradient(180deg, #ffffff 0%, #f3f3f3 22%, #e9dcd3 45%, #d9b49c 100%);
  }
  .tagline {
    position: absolute; top: 12px; left: 0; right: 0;
    text-align: center;
    font-size: 62px; font-weight: 900; letter-spacing: 2px;
    color: var(--orange);
  }
  .title-line {
    position: absolute; left: 0; right: 0;
    text-align: center;
    font-weight: 900;
    color: var(--orange);
    -webkit-text-stroke: 14px var(--white);
    paint-order: stroke fill;
  }
  .title-line--upper { top: 88px; font-size: 104px; letter-spacing: 2px; }
  .title-line--lower { top: 322px; font-size: 116px; letter-spacing: 4px; }
  .title-tiles {
    position: absolute; top: 206px; left: 0; right: 0;
    display: flex; justify-content: center; gap: 6px;
  }
  .tile {
    width: 124px; height: 118px;
    display: flex; align-items: center; justify-content: center;
    font-size: 96px; font-weight: 900; color: var(--white);
    border: 5px solid var(--white);
  }
  .tile--green { background: var(--green); transform: rotate(-4deg); }
  .tile--pink  { background: var(--pink);  transform: rotate(3deg) translateY(-6px); }
  .tile--blue  { background: var(--blue);  transform: rotate(-3deg); }
  .tile--red   { background: var(--red);   transform: rotate(4deg) translateY(-4px); }
  .author {
    position: absolute; top: 518px; left: 330px;
    display: flex; align-items: center; gap: 10px;
    font-size: 34px; font-weight: 800; color: var(--gray);
  }
  .author-mark {
    width: 34px; height: 34px;
    background: var(--orange); color: var(--white);
    font-size: 22px; display: flex; align-items: center; justify-content: center;
  }
  .bubble {
    position: absolute;
    border-radius: 50%;
    display: flex; align-items: center; justify-content: center;
    text-align: center;
    color: var(--white); font-weight: 800; line-height: 1.25;
  }
  .bubble--red   { left: 574px; top: 530px; width: 166px; height: 166px; background: var(--red); font-size: 29px; }
  .bubble--green { left: 516px; top: 676px; width: 184px; height: 184px; background: var(--green); font-size: 30px; }
  .bubble--pink  { left: 26px;  top: 852px; width: 184px; height: 184px; background: var(--pink); font-size: 30px; }
</style>
</head>
<body>
  <main class="cover">
    <div class="cover-photo" role="img" aria-label="大きく口を開けて笑う女性の写真と、放射状の集中線の背景"></div>

    <p class="tagline">週末ごとに和みを探す</p>
    <h1>
      <span class="title-line title-line--upper">読者へ贈る</span>
      <span class="title-tiles">
        <span class="tile tile--green">癒</span>
        <span class="tile tile--pink">や</span>
        <span class="tile tile--blue">し</span>
        <span class="tile tile--red">の</span>
      </span>
      <span class="title-line title-line--lower">四季手帳</span>
    </h1>

    <p class="author"><span class="author-mark">著</span>○○○○</p>

    <p class="bubble bubble--red">猫の昼寝は<br>街を<br>照らす</p>
    <p class="bubble bubble--green">私は<br>猫の昼寝に<br>癒された</p>
    <p class="bubble bubble--pink">猫の昼寝は<br>毎日を<br>照らす</p>
  </main>
</body>
</html>
```